もみほぐし、マッサージ店の看板デザイン(二種類)を依頼させて頂きます。

1.店舗に設置するヨコ看板   横350cm×縦75cm
2.店外に設置するスタンド看板 横42cm×縦113cm
(設置位置は添付画像をご覧ください、また参考程度に添付エクセルをご覧くださいませ)

場所は、県では一番賑わっているアーケード内の繁華街となります。
誰でもお越しいただける「安心感、癒し、やわらかさ」と
街中ですので「多少の洗練」を希望いたします。
一目で「マッサージ、指圧、もみほぐし」と直感できると嬉しいです。

店内は明るいライムグリーンを基調としておりますが、
ブランド力はありませんので、目につきやすい配色で人目を引ければと思います。

準備中ではございますが、店内の画像も添付いたしましたのでご覧ください。

会社名  フワリK 桜木通り店
電話番号 096-555-0172
営業時間 朝10時から翌朝5時

・「全身ほぐしコース 60分 税込 2980円」

・価格テーブル(添付エクセルデータをご覧ください)

・「深夜0時以降は、プラス100円いただきます」

・エレベータをのぼって2階にあるため「2F」

・ロゴ等はなにぶん開業前ですので、特にございません。

文言で強調していただきたいポイントは
「全身ほぐしコース60分2980円」の割安感と
2回にあるため「2F」というところです。
明るめのライムグリーン、強調する意味での赤など。他にも良い案をご提案下さい。
なにぶん初めての依頼ですので、いたらない部分もあるかと思いますが、誠実に対応させていただきますので、どうぞよろしくお願いいたします。
すみません。
記載項目の記述は、スタンド看板だけを念頭に置いて書いてしまいました。

ヨコ看板に最低限載せていただきたい記載文言は

・店舗名 フワリK 桜木通店
・全身(※もみ)ほぐし(※コース)60分 税込 2980円
・電話番号 096-555-0172

の3つとなります(※は必須ではございません)
よろしくお願いいたします。
時間も差し迫ったところで、申し訳ございませんが、
強く希望させていただきたいポイントと
変更内容を追記いたします。

【希望】
1)上部のヨコ看板についてですが
店名等より「全身もみほぐし 60分 2980円(税込)」
という文言を、より大きく前面に押し出していただきたいです。
(税込)もお願いいたします。

2)下のスタンド看板についてです。
価格テーブルを必ず載せて欲しいです。
(もみほぐし)(足つぼ)(もみほぐし&足つぼハーフ)(眼精疲労コース)
以上の4種類です。

3)写真についての希望です。
当店ではお客様任意の動きやすい服装か、ジャージをお貸しして
その上からタオルを載せて施術するという形をとりますので
素材がございましたら、着衣の画像をお願いいたします。
これはあくまで希望で必須ではありません。

4)店名について。
「フワリ」はカタカナ。「M」はアルファベットをお願いいたします。

【変更】
眼精疲労コースの時間と料金を変更いたします。
「15分1080円」となります。
価格テーブルのエクセルファイルをアップロードいたしますのでご覧ください。

以上よろしくお願い申し上げます。
こちらの説明不足でご迷惑をおかけします。
(マッサージ)という言葉が法律に抵触する可能性も考えられます。
(マッサージ)という単語は看板では使わない方向で考えておりますので
よろしくお願いいたします。
募集終了後、当選候補者様をお選びし修正依頼を
お送り致しますが少々急いでおりますので納品を
明日、11日15時までにお願いしたいと考えております。
もし修正依頼を受け取られた候補者様のスケジュールが
合わず、11日15時に間に合わないと判断された場合は
即座にお断りのご連絡を頂けましたら幸いです。
こちらの勝手な都合を押しつけるようで誠に恐縮ですが
よろしく申し上げます。

配色、デザインが最も洗練されていると感じました。
一目で気に入りました。
親指を鳥の目に見立てた「M」のロゴマークも素晴らしいと思いました。

こちらの度重なる修正依頼にも迅速に、誠実に対応して頂きました。

予想を超えるご応募をいただき誠に感謝しております。
たくさん良いデザインがありましたので一つお選びするのは
大変心苦しかったです。

皆さまありがとうございました。

```html
<!DOCTYPE html>
<html lang="ja">
<head>
<meta charset="utf-8">
<title>フワリK 桜木通店 スタンド看板</title>
<link href="https://fonts.googleapis.com/css2?family=Noto+Sans+JP:wght@500;700;900&family=Noto+Serif+JP:wght@600;700&display=swap" rel="stylesheet">
<style>
:root{
  --green:#4fae2b;
  --green-deep:#2f8a1c;
  --green-light:#8cc63f;
  --red:#e60012;
  --yellow:#fff100;
  --white:#ffffff;
  --orange:#e8780a;
  --pink:#e4007f;
  --blue:#0095d9;
  --purple:#b0208c;
  --ink:#222;
}
*{margin:0;padding:0;box-sizing:border-box}
html,body{width:1200px;height:3220px;overflow:hidden}
body{font-family:"Noto Sans JP",sans-serif;background:var(--green-light);position:relative}
.header{position:absolute;left:0;top:0;width:1200px;height:420px;
  background:linear-gradient(180deg,var(--green) 0%,#62bd35 100%)}
.shop-mark{position:absolute;left:410px;top:20px;width:380px;height:380px;border-radius:50%;
  background:var(--white);display:flex;flex-direction:column;align-items:center;justify-content:center;
  color:var(--green-deep);font-weight:700;z-index:3;line-height:1.05}
.shop-mark .kana{font-size:60px;letter-spacing:6px}
.shop-mark .initial{font-size:150px}
.shop-mark .branch{font-size:50px;letter-spacing:4px}
.photo{position:absolute;left:40px;top:380px;width:1120px;height:840px;
  background:linear-gradient(160deg,#f1f1ec 0%,#d9dcd3 45%,#8b6a55 80%,#5d4334 100%)}
.badge-2f{position:absolute;left:840px;top:1130px;width:310px;height:200px;background:var(--red);
  border:10px solid var(--white);border-radius:14px;transform:rotate(-6deg);z-index:4;
  color:var(--white);font-weight:900;font-size:170px;line-height:180px;text-align:center}
.offer{position:absolute;left:0;top:1290px;width:1200px;height:400px;background:var(--red)}
.offer-title{position:absolute;left:40px;top:40px;font-weight:900;font-size:136px;line-height:1;white-space:nowrap;
  color:var(--yellow);letter-spacing:-4px;-webkit-text-stroke:4px #b3000e;paint-order:stroke fill}
.offer-title small{font-size:48px;letter-spacing:0;-webkit-text-stroke:0;color:var(--yellow)}
.offer-price{position:absolute;left:40px;top:210px;width:1120px;height:170px;background:var(--white);
  border-radius:10px;display:flex;align-items:center;justify-content:center;color:var(--red);font-weight:900}
.offer-price .big{font-size:160px;letter-spacing:-6px;line-height:1;white-space:nowrap}
.offer-price .tax{writing-mode:vertical-rl;font-size:34px;font-weight:700;margin-left:10px}
.price-table{position:absolute;left:80px;top:1790px;border-collapse:separate;border-spacing:8px;
  font-family:"Noto Serif JP",serif}
.price-table th{background:var(--white);height:160px;font-family:"Noto Sans JP",sans-serif;
  font-size:38px;font-weight:700;line-height:1.2}
.price-table td{height:102px;font-size:64px;font-weight:700;text-align:right;padding-right:22px;background:var(--white)}
.price-table .min{width:88px;text-align:center;padding:0;color:var(--ink);font-size:46px;font-family:"Noto Sans JP",sans-serif}
.price-table td.empty{background:var(--green)}
.price-table .c1{width:220px;color:var(--orange)}
.price-table .c2{width:240px;color:var(--pink)}
.price-table .c3{width:240px;color:var(--blue)}
.price-table .c4{width:250px;color:var(--purple)}
.fees{position:absolute;left:80px;top:2640px;width:1060px;display:flex;justify-content:space-between;
  font-size:46px;font-weight:700;color:var(--ink)}
.fees .yen{color:var(--red)}
.notes{position:absolute;left:80px;top:2715px;font-size:34px;font-weight:500;color:var(--ink);line-height:1.5}
.hours{position:absolute;left:50px;top:2850px;display:flex;align-items:center;gap:10px;white-space:nowrap}
.hours .tag{width:80px;height:80px;border-radius:50%;background:var(--white);color:var(--green-deep);
  font-size:50px;font-weight:900;display:flex;align-items:center;justify-content:center;flex:none}
.hours .time{margin-left:20px;font-size:84px;font-weight:900;color:var(--white);letter-spacing:-1px;line-height:1}
.phone{position:absolute;left:50px;top:2990px;display:flex;align-items:center;gap:20px;white-space:nowrap}
.phone svg{width:120px;height:120px;flex:none}
.phone .number{font-size:140px;font-weight:900;color:var(--white);letter-spacing:-2px;line-height:1}
</style>
</head>
<body>
<header class="header">
  <div class="shop-mark">
    <span class="kana">フワリ</span>
    <span class="initial">K</span>
    <span class="branch">桜木通店</span>
  </div>
</header>
<div class="photo" role="img" aria-label="明るいライムグリーンの店内に施術ベッドが並ぶ写真"></div>
<div class="badge-2f">2F</div>

<section class="offer">
  <h1 class="offer-title">全身もみほぐし<small>コース</small></h1>
  <div class="offer-price"><span class="big">60分2980円</span><span class="tax">(税込)</span></div>
</section>

<table class="price-table">
  <thead>
    <tr>
      <th class="min">分</th>
      <th class="c1">もみほぐし<br>コース</th>
      <th class="c2">もみほぐし<br>コース</th>
      <th class="c3">もみほぐし<br>コース</th>
      <th class="c4">眼精疲労<br>コース</th>
    </tr>
  </thead>
  <tbody>
    <tr><td class="min">15</td><td class="c1">980</td><td class="empty"></td><td class="empty"></td><td class="c4">1,080</td></tr>
    <tr><td class="min">30</td><td class="c1">1,780</td><td class="c2">2,280</td><td class="empty"></td><td class="empty"></td></tr>
    <tr><td class="min">45</td><td class="c1">2,480</td><td class="c2">2,980</td><td class="empty"></td><td class="empty"></td></tr>
    <tr><td class="min">60</td><td class="c1">2,980</td><td class="c2">3,580</td><td class="c3">3,380</td><td class="empty"></td></tr>
    <tr><td class="min">90</td><td class="c1">4,680</td><td class="c2">5,380</td><td class="c3">4,980</td><td class="empty"></td></tr>
    <tr><td class="min">120</td><td class="c1">6,280</td><td class="c2">7,180</td><td class="c3">6,680</td><td class="empty"></td></tr>
  </tbody>
</table>

<div class="fees">
  <span>★個人指名料　<span class="yen">¥300</span></span>
  <span>★男女指名料　<span class="yen">¥100</span></span>
</div>
<p class="notes">●表示価格はすべて税込価格です。<br>●深夜12時以降は、合計金額よりプラス100円を頂きます。</p>

<div class="hours">
  <span class="tag">営</span><span class="tag">業</span><span class="tag">時</span><span class="tag">間</span>
  <span class="time">朝10時〜翌朝5時</span>
</div>

<div class="phone">
  <svg viewBox="0 0 100 100" aria-hidden="true">
    <circle cx="50" cy="50" r="48" fill="#fff"/>
    <path d="M34 24c3-2 7-1 8 2l4 10c1 3 0 5-2 7l-4 3c3 7 8 12 15 15l3-4c2-2 4-3 7-2l10 4c3 1 4 5 2 8l-4 5c-3 3-8 4-12 2-17-7-29-19-36-36-2-4-1-9 2-12z" fill="#2f8a1c"/>
  </svg>
  <span class="number">096-555-0172</span>
</div>
</body>
</html>
```